Keystone Ridge Construction LLC

We need a professional and colorful website that describes our company [please see below]:

CORE COMPETENCIES

About Us: Keystone Ridge Construction, LLC is a veteran-owned business, and is a leading force in the construction industry. We have continuously provided exceptional services to our clients. With a wealth of experience and a commitment of excellence, we have earned a reputation for delivering high-quality projects on time and within budget.

Core Competencies:

Experience: With decades of experience, we bring unparalleled expertise to every project we undertake. Our team consists of seasoned professionals who are experts in their respective fields.

Portfolio: Our portfolio encompasses a wide range of construction projects, including commercial building, industrial facilities, infrastructure development and more.

KEYSTONE RIDGE: We stay at the forefront of industry trends and technologies, leveraging the latest tools and techniques to deliver innovative solutions.

Client Satisfaction: Our commitment to client satisfaction is unwavering. We prioritize open communication, transparency, and responsiveness, working closely with clients to understand their needs and deliver results.

Safety: Safety is our top priority on every job site. We adhere to the highest safety standards and implement rigorous safety protocols to ensure the well-being of our workers and stakeholders.

KEY SERVICES

General Contracting
Construction Management
Design-Build Services
Pre-construction Planning
Value Engineering
Sustainable Construction Practices
Renovation and Remodeling
Quality Assurance and Control
Project Estimating and Budgeting
Permitting and Regulatory Compliance

CONTACT INFORMATION

Douglas Whitfield, President
Email Address [TBD]
Website Address [TBD]
555.214.6093

Federal Government and Commercial Agencies

Construction and Design Build

• Please use our attached logo and color scheme that was designed through Pixel Forum. Please include the Nation's Capitol building with a patriotic feel and include a diverse work force. Include federal buildings in the pictures. Please include in the opeing tagline that the company is Veteran Owned.

```html
<!DOCTYPE html>
<html lang="en">
<head>
<meta charset="utf-8">
<title>Keystone Ridge Construction, LLC</title>
<link href="https://fonts.googleapis.com/css2?family=Libre+Baskerville:wght@400;700&family=Poppins:wght@400;500&display=swap" rel="stylesheet">
<style>
:root{
  --navy:#232a66;
  --navy-deep:#1a2050;
  --green:#8cc63f;
  --paper:#efebeb;
  --ink:#4a4a55;
  --white:#ffffff;
}
*{margin:0;padding:0;box-sizing:border-box}
html,body{width:1200px;height:3385px;overflow:hidden}
body{position:relative;background:var(--white);font-family:'Poppins',sans-serif;color:var(--ink)}
.serif{font-family:'Libre Baskerville',serif}
.abs{position:absolute}

/* hero */
.hero-photo{position:absolute;left:0;top:0;width:1200px;height:725px;
  clip-path:polygon(0 0,100% 0,100% 725px,0 614px);
  background:linear-gradient(160deg,#1c2549 0%,#2d3a5e 35%,#5b6372 65%,#8a8478 100%)}
.hero-shade{position:absolute;left:0;top:0;width:1200px;height:725px;
  clip-path:polygon(0 0,100% 0,100% 725px,0 614px);
  background:linear-gradient(90deg,rgba(20,26,60,.75) 0%,rgba(20,26,60,.35) 60%,rgba(20,26,60,.1) 100%)}
.topbar-line{position:absolute;left:0;top:55px;width:1200px;height:1px;background:rgba(255,255,255,.45)}
.topbar-item{position:absolute;top:21px;font-family:'Libre Baskerville',serif;font-size:13px;letter-spacing:1px;color:var(--white);display:flex;align-items:center;gap:10px}
.topbar-sep{position:absolute;top:14px;width:1px;height:32px;background:rgba(255,255,255,.6)}
.brand{position:absolute;font-family:'Libre Baskerville',serif;font-weight:400;color:var(--white);text-align:center;line-height:1}
.nav a{position:absolute;top:115px;font-family:'Libre Baskerville',serif;font-size:12px;color:var(--white);text-decoration:none;letter-spacing:.3px}
.nav a.active{color:var(--green)}
.btn{position:absolute;display:flex;align-items:center;justify-content:center;font-family:'Libre Baskerville',serif;font-size:14px;color:var(--white);letter-spacing:.5px;text-decoration:none}
.btn::before{content:"";position:absolute;inset:0;background:var(--green);transform:skewX(-22deg);z-index:-1}
.btn{z-index:1}
.hero-title{position:absolute;left:109px;top:222px;font-family:'Libre Baskerville',serif;font-weight:700;font-size:52px;line-height:68px;color:var(--white)}
.scroll-down{position:absolute;left:565px;top:644px}

/* about */
.about-photo{position:absolute;left:155px;top:683px;width:420px;height:558px;
  background:linear-gradient(180deg,#c9d7e4 0%,#9fb4c8 40%,#2b3450 70%,#1d2236 100%);
  clip-path:polygon(0 160px,38% 0,100% 0,100% 100%,0 100%)}
.section-title{font-family:'Libre Baskerville',serif;font-weight:700;color:var(--navy);letter-spacing:.5px}
.rule{position:absolute;height:1px;background:var(--green)}
.about-text{position:absolute;left:639px;top:966px;width:412px;font-size:13.6px;line-height:21px;color:var(--ink)}

/* competencies */
.comp-bg{position:absolute;left:0;top:1310px;width:1200px;height:774px;background:var(--paper);
  clip-path:polygon(0 0,100% 0,100% 665px,0 100%)}
.card{position:absolute;top:1498px;width:233px;height:408px;background:var(--white);
  clip-path:polygon(0 0,100% 0,100% 93%,0 100%)}
.card-img{width:100%;height:205px}
.card h3{position:absolute;left:24px;top:236px;font-family:'Libre Baskerville',serif;font-size:15px;letter-spacing:1.2px;color:var(--navy);font-weight:400}
.card p{position:absolute;left:24px;top:272px;width:195px;font-size:13.4px;line-height:21px;color:var(--ink)}
.card .more{position:absolute;left:24px;top:349px;font-family:'Libre Baskerville',serif;font-size:11.5px;letter-spacing:1px;color:var(--green);font-weight:700}
.pager{position:absolute;top:1950px;width:38px;height:36px;display:flex;align-items:center;justify-content:center}

/* services */
.service{position:absolute;display:flex;align-items:center;gap:16px}
.service .label{font-family:'Libre Baskerville',serif;font-size:16px;line-height:21px;letter-spacing:1.2px;color:var(--navy)}
.service.right{flex-direction:row;text-align:right}
.service svg{flex:none}

/* cta */
.footer-band{position:absolute;left:0;top:2865px;width:1200px;height:520px;background:var(--navy);
  clip-path:polygon(0 80px,100% 0,100% 100%,0 100%)}
.cta-photo{position:absolute;left:0;top:0;width:1200px;height:3385px;
  clip-path:polygon(168px 2723px,1086px 2715px,999px 3019px,112px 3025px);
  background:linear-gradient(100deg,#8a6b34 6%,#5a5d56 30%,#2f5566 55%,#1d4d63 80%,#1a3f58 100%)}
.cta-shade{position:absolute;left:0;top:0;width:1200px;height:3385px;
  clip-path:polygon(168px 2723px,1086px 2715px,999px 3019px,112px 3025px);
  background:rgba(20,30,60,.35)}
.cta-title{position:absolute;left:0;width:1200px;top:2792px;text-align:center;font-family:'Libre Baskerville',serif;font-weight:700;font-size:42px;color:var(--white)}
.cta-text{position:absolute;left:0;width:1200px;top:2847px;text-align:center;font-size:13.6px;line-height:21px;color:var(--white)}

/* footer */
.foot-head{position:absolute;top:3104px;font-family:'Libre Baskerville',serif;font-weight:700;font-size:18px;color:var(--white);letter-spacing:.5px}
.quick a{position:absolute;left:474px;font-size:10px;color:var(--white);text-decoration:none}
.email-input{position:absolute;left:689px;top:3146px;width:284px;height:44px;background:var(--white);border-radius:3px;font-size:11px;color:#9a9aa4;padding:16px 20px}
.subscribe{position:absolute;left:978px;top:3146px;width:109px;height:44px;background:var(--green);border-radius:3px;font-family:'Libre Baskerville',serif;font-size:14px;color:var(--white);display:flex;align-items:center;justify-content:center}
.social{position:absolute;top:3206px;width:36px;height:36px;border-radius:50%;background:#5c7a3a}
.foot-rule{position:absolute;left:188px;top:3296px;width:850px;height:1px;background:rgba(255,255,255,.3)}
.copyright{position:absolute;left:0;width:1200px;top:3334px;text-align:center;font-family:'Libre Baskerville',serif;font-size:14px;color:var(--white)}
</style>
</head>
<body>

<!-- hero -->
<div class="hero-photo" role="img" aria-label="Photo of the Capitol building steps under a dramatic sky"></div>
<div class="hero-shade"></div>

<div class="topbar-item" style="left:334px">
  <svg width="12" height="12" viewBox="0 0 24 24"><path fill="#8cc63f" d="M6.6 10.8a15.1 15.1 0 006.6 6.6l2.2-2.2a1 1 0 011-.25 11.4 11.4 0 003.6.57 1 1 0 011 1V20a1 1 0 01-1 1A17 17 0 013 4a1 1 0 011-1h3.5a1 1 0 011 1 11.4 11.4 0 00.57 3.6 1 1 0 01-.25 1z"/></svg>
  <span>555.214.6093</span>
</div>
<div class="topbar-sep" style="left:511px"></div>
<div class="topbar-item" style="left:536px">
  <svg width="12" height="10" viewBox="0 0 24 18"><path fill="#8cc63f" d="M0 0h24v2.5L12 10 0 2.5zM0 5l12 7.5L24 5v13H0z"/></svg>
  <span>Email info@keystoneridgebuild.com</span>
</div>
<div class="topbar-sep" style="left:863px"></div>
<div class="topbar-item" style="left:896px">
  <svg width="10" height="13" viewBox="0 0 20 26"><path fill="#8cc63f" d="M10 0a10 10 0 00-10 10c0 7.5 10 16 10 16s10-8.5 10-16A10 10 0 0010 0zm0 14a4 4 0 110-8 4 4 0 010 8z"/></svg>
  <span>Website Address [TBD]</span>
</div>
<div class="topbar-line"></div>

<div class="brand" style="left:108px;top:88px;width:218px">
  <div style="font-size:25px;letter-spacing:1px">KEYSTONE RIDGE</div>
  <div style="font-size:9px;letter-spacing:1.3px;margin-top:8px">CONSTRUCTION, LLC</div>
</div>

<nav class="nav">
  <a class="active" style="left:365px">HOME</a>
  <a style="left:443px">ABOUT US</a>
  <a style="left:545px">KEY SERVICES</a>
  <a style="left:674px">CORE COMPETENCIES</a>
  <a style="left:856px">CONTACT</a>
</nav>
<a class="btn" style="left:950px;top:99px;width:128px;height:46px">CONTACT</a>

<h1 class="hero-title">INNOVATING<br>EXCELLENCE PROUDLY<br>VETERAN-OWNED</h1>
<a class="btn" style="left:117px;top:480px;width:160px;height:46px">CONTACT US</a>

<svg class="scroll-down" width="69" height="59" viewBox="0 0 69 59">
  <polygon points="0,0 69,0 34.5,59" fill="#8cc63f"/>
  <path d="M34.5 12v20M27 25l7.5 7.5L42 25" stroke="#fff" stroke-width="2.2" fill="none"/>
</svg>

<!-- about -->
<div class="about-photo" role="img" aria-label="Portrait of the company president in a navy suit before office towers"></div>
<h2 class="section-title abs" style="left:639px;top:890px;font-size:40px">ABOUT US</h2>
<div class="rule" style="left:639px;top:953px;width:117px"></div>
<p class="about-text">Keystone Ridge Construction, LLC is a veteran-owned business, and is a leading force in the construction industry. We have continuously provided exceptional services to our clients. With a wealth of experience and a commitment of excellence, we have earned a reputation for delivering high-quality projects on time and within budget</p>
<a class="btn" style="left:647px;top:1128px;width:162px;height:46px">READ MORE</a>

<!-- core competencies -->
<div class="comp-bg"></div>
<h2 class="section-title abs" style="left:0;width:1200px;text-align:center;top:1400px;font-size:42px">CORE COMPETENCIES</h2>
<div class="rule" style="left:541px;top:1467px;width:117px"></div>

<article class="card" style="left:108px">
  <div class="card-img" role="img" aria-label="Photo of a diverse team reviewing blueprints" style="background:linear-gradient(135deg,#c8d4e0,#3a4f7a 55%,#2a3350)"></div>
  <h3>EXPERIENCE</h3>
  <p>With decades of experience, we bring unparalleled expertise to every project we...</p>
  <span class="more">READ MORE</span>
</article>
<article class="card" style="left:356px">
  <div class="card-img" role="img" aria-label="Photo of an engineer with a tablet at a construction site" style="background:linear-gradient(135deg,#b88a6a,#d9d2c8 55%,#eef0f2)"></div>
  <h3>PORTFOLIO</h3>
  <p>Our portfolio encompasses a wide range of construction projects, including...</p>
  <span class="more">READ MORE</span>
</article>
<article class="card" style="left:605px">
  <div class="card-img" role="img" aria-label="Photo of engineers in hard hats discussing plans" style="background:linear-gradient(135deg,#3c3a3a,#9a9c98 50%,#d8d4cc)"></div>
  <h3>INNOVATION</h3>
  <p>We stay at the forefront of industry trends and technologies, leveraging...</p>
  <span class="more">READ MORE</span>
</article>
<article class="card" style="left:853px">
  <div class="card-img" role="img" aria-label="Photo of a site worker in safety vest with a manager" style="background:linear-gradient(135deg,#c7ccd2,#e07a2a 45%,#4a4f5a)"></div>
  <h3>SAFETY</h3>
  <p>Safety is our top priority on every job site. We adhere to the highest safety...</p>
  <span class="more">READ MORE</span>
</article>

<div class="pager" style="left:557px;background:var(--green)"><svg width="10" height="12" viewBox="0 0 10 12"><path d="M7 1L2 6l5 5" stroke="#fff" stroke-width="2" fill="none"/></svg></div>
<div class="pager" style="left:605px;background:var(--navy)"><svg width="10" height="12" viewBox="0 0 10 12"><path d="M3 1l5 5-5 5" stroke="#fff" stroke-width="2" fill="none"/></svg></div>

<!-- key services -->
<h2 class="section-title abs" style="left:0;width:1200px;text-align:center;top:2140px;font-size:42px">KEY SERVICES</h2>
<div class="rule" style="left:541px;top:2207px;width:117px"></div>

<g></g>
<div class="service" style="left:140px;top:2237px">
  <svg width="52" height="46" viewBox="0 0 52 46" fill="none" stroke="#8cc63f" stroke-width="2"><rect x="4" y="10" width="44" height="34"/><path d="M4 10l6-8h32l6 8M12 20h10v10H12zM30 20h10v24H30"/></svg>
  <div class="label">GENERAL<br>CONTRACTING</div>
</div>
<div class="service" style="left:137px;top:2320px">
  <svg width="52" height="50" viewBox="0 0 52 50" fill="none" stroke="#8cc63f" stroke-width="2"><path d="M10 24L28 8l18 16M16 20v18h24V20M22 38V28h12v10M4 44c8-6 18-6 26-2"/></svg>
  <div class="label">CONSTRUCTION<br>MANAGEMENT</div>
</div>
<div class="service" style="left:137px;top:2410px">
  <svg width="52" height="52" viewBox="0 0 52 52" fill="none" stroke="#8cc63f" stroke-width="2"><path d="M4 50h44M8 50V22h12v28M22 50V6h16v44M40 50V28h8v22M12 28h4M12 36h4M26 14h8M26 22h8M26 30h8M26 38h8"/></svg>
  <div class="label">DESIGN-BUILD<br>SERVICES</div>
</div>
<div class="service" style="left:137px;top:2492px">
  <svg width="52" height="52" viewBox="0 0 52 52" fill="none" stroke="#8cc63f" stroke-width="2"><circle cx="26" cy="26" r="14"/><circle cx="26" cy="26" r="6"/><path d="M26 4v8M26 40v8M4 26h8M40 26h8M10 10l6 6M36 36l6 6M42 10l-6 6M16 36l-6 6"/></svg>
  <div class="label">PRE-CONSTRUCTION<br>PLANNING</div>
</div>
<div class="service" style="left:137px;top:2576px">
  <svg width="52" height="52" viewBox="0 0 52 52" fill="none" stroke="#8cc63f" stroke-width="2"><path d="M4 50h44M10 50V34h6v16M22 50V26h6v24M34 50V18h6v32M8 22l12-10 8 6 16-14M38 4h6v6"/></svg>
  <div class="label">VALUE<br>ENGINEERING</div>
</div>

<div class="service right" style="right:142px;top:2234px">
  <div class="label">SUSTAINABLE<br>CONSTRUCTION PRACTICES</div>
  <svg width="52" height="52" viewBox="0 0 52 52" fill="none" stroke="#8cc63f" stroke-width="2"><circle cx="26" cy="28" r="18"/><path d="M26 46V24M26 32c-6 0-10-4-10-10 6 0 10 4 10 10zM26 28c0-6 4-10 10-10 0 6-4 10-10 10zM26 2v8"/></svg>
</div>
<div class="service right" style="right:142px;top:2318px">
  <div class="label">PERMITTING AND<br>REGULATORY COMPLIANCE</div>
  <svg width="52" height="52" viewBox="0 0 52 52" fill="none" stroke="#8cc63f" stroke-width="2"><path d="M10 18l12-12 8 8-12 12zM24 20l20 20-4 4-20-20M4 48h26M8 48v-6h18v6"/></svg>
</div>
<div class="service right" style="right:142px;top:2410px">
  <div class="label">QUALITY ASSURANCE<br>AND CONTROL</div>
  <svg width="52" height="52" viewBox="0 0 52 52" fill="none" stroke="#8cc63f" stroke-width="2"><circle cx="18" cy="32" r="12"/><circle cx="18" cy="32" r="4"/><circle cx="36" cy="16" r="10"/><circle cx="36" cy="16" r="3"/><path d="M40 38l4 4 6-8"/></svg>
</div>
<div class="service right" style="right:142px;top:2492px">
  <div class="label">PROJECT ESTIMATING<br>AND BUDGETING</div>
  <svg width="52" height="52" viewBox="0 0 52 52" fill="none" stroke="#8cc63f" stroke-width="2"><rect x="22" y="22" width="26" height="26"/><path d="M22 30h26M22 38h26M31 22v26M40 22v26M6 4h20v10H6zM16 14v20"/><circle cx="12" cy="40" r="8"/><path d="M12 35v10"/></svg>
</div>
<div class="service right" style="right:142px;top:2576px">
  <div class="label">RENOVATION<br>AND REMODELING</div>
  <svg width="58" height="52" viewBox="0 0 58 52" fill="none" stroke="#8cc63f" stroke-width="2"><path d="M4 26L29 4l25 22M10 22v26h38V22M22 48V32h14v16M38 12V6h6v11"/></svg>
</div>

<!-- call to action -->
<div class="footer-band"></div>
<div class="cta-photo" role="img" aria-label="Photo looking up at glass office towers at sunset"></div>
<div class="cta-shade"></div>
<h2 class="cta-title">READY TO START YOUR PROJECT?</h2>
<p class="cta-text">Get in touch with us today to discuss your construction needs. Our team of experts is here<br>to bring your vision to life.</p>
<a class="btn" style="left:517px;top:2914px;width:160px;height:46px">CONTACT US</a>

<!-- footer -->
<div class="brand" style="left:109px;top:3200px;width:290px">
  <div style="font-size:33px;letter-spacing:1px">KEYSTONE RIDGE</div>
  <div style="font-size:11px;letter-spacing:1.6px;margin-top:10px">CONSTRUCTION, LLC</div>
</div>

<div class="foot-head" style="left:474px">QUICK LINKS</div>
<nav class="quick">
  <a style="top:3148px">HOME</a>
  <a style="top:3173px">ABOUT US</a>
  <a style="top:3198px">CORE COMPETENCIES</a>
  <a style="top:3223px">KEY SERVICES</a>
  <a style="top:3248px">CONTACT</a>
</nav>

<div class="foot-head" style="left:691px">FOLLOW UP</div>
<div class="email-input">Enter Your email</div>
<div class="subscribe">SUBMAIL</div>
<div class="social" style="left:697px;background:var(--green)" aria-label="Social profile"></div>
<div class="social" style="left:740px" aria-label="Social profile"></div>
<div class="social" style="left:785px" aria-label="Social profile"></div>
<div class="social" style="left:830px" aria-label="Social profile"></div>

<svg class="abs" style="left:1086px;top:3274px" width="38" height="36" viewBox="0 0 38 36">
  <path d="M19 2C9 2 2 8 2 16c0 4 2 8 6 10l-2 8 9-6c1 0 3 .3 4 .3 10 0 17-6 17-13S29 2 19 2z" fill="#8cc63f"/>
  <circle cx="12" cy="16" r="2.2" fill="#fff"/><circle cx="19" cy="16" r="2.2" fill="#fff"/><circle cx="26" cy="16" r="2.2" fill="#fff"/>
</svg>

<div class="foot-rule"></div>
<div class="copyright">©2024 KEYSTONE RIDGE CONSTRUCTION, LLC</div>

</body>
</html>
```